New professional looking flyer for company

I need our flyer updated my flyer is the Ruv flyer Have attached current flyer so you know what services need to be listed. Want it to be in mainly dark colours like black and dark grey with pops of light grey, silver or white. i have added several photos for you to choose which ones work best with your design would like The photos to be in colour for the flyer. But can have a mix of greyscale if that works for your design j have attached another companies flyers as design ideas to show what I am looking for

Target Market(s)

new clients

Industry/Entity Type

transport and earthmoving

Colors

Designer to choose colors to be used in the design.

Requirements
Nice to have
• Look professional
Should not have
• No orange or red or green

```html
<!DOCTYPE html>
<html lang="en">
<head>
<meta charset="utf-8">
<title>RUV Pty Ltd Flyer</title>
<link href="https://fonts.googleapis.com/css2?family=Saira+Condensed:wght@500;600;700;800&display=swap" rel="stylesheet">
<style>
:root{
  --stage:#58585a;
  --ink:#000;
  --charcoal:#141414;
  --silver-light:#eeeeee;
  --silver-mid:#c7c8ca;
  --silver-dark:#8d8e90;
  --white:#ffffff;
  --panel:#dcdddf;
}
*{margin:0;padding:0;box-sizing:border-box}
html,body{width:892px;height:1200px;overflow:hidden;background:var(--stage)}
body{font-family:"Saira Condensed",sans-serif;position:relative}
.flyer{position:absolute;left:71px;top:63px;width:750px;height:1060px;background:var(--ink);overflow:hidden;box-shadow:6px 8px 14px rgba(0,0,0,.45)}
.flyer-art{position:absolute;inset:0}
.abs{position:absolute}
.brand-name{left:0;width:750px;top:48px;text-align:center;font-size:112px;font-weight:800;line-height:1;color:var(--silver-mid);letter-spacing:-2px}
.brand-suffix{left:0;width:750px;top:150px;text-align:center;font-size:32px;font-weight:600;color:var(--silver-mid);line-height:1}
.services-tab{left:457px;top:417px;width:206px;height:73px;background:var(--ink);border-radius:0 0 12px 12px;color:var(--white);font-size:29px;font-weight:700;text-align:center;padding-top:36px;line-height:1}
.services-list{left:418px;top:505px;width:286px;list-style:none}
.services-list li{display:flex;align-items:flex-start;gap:10px;font-size:18.5px;font-weight:600;color:var(--charcoal);line-height:17px;padding:4px 0 4px 0;border-bottom:1px solid #b5b6b8;min-height:26px}
.services-list li svg{flex:0 0 16px;margin-top:0}
.capable{left:47px;top:566px;font-size:35px;font-weight:700;color:var(--white);line-height:34px}
.supply-list{left:47px;top:648px;font-size:38px;font-weight:800;line-height:36px;background:linear-gradient(90deg,#ffffff 0%,#bfbfbf 45%,#ffffff 60%,#9a9a9a 80%,#ffffff 100%);-webkit-background-clip:text;background-clip:text;color:transparent;letter-spacing:.5px}
.rule{height:1px;background:linear-gradient(90deg,#8a8a8a,#2a2a2a)}
.note{left:37px;top:974px;font-size:18.5px;font-weight:600;color:var(--white);line-height:20px}
.cta{left:37px;top:996px;font-size:22px;font-weight:600;color:var(--white);line-height:24px;letter-spacing:.5px}
.phone{left:507px;top:972px;font-size:39px;font-weight:800;color:var(--ink);line-height:46px;letter-spacing:1px}
.contact{right:46px;top:1023px;font-size:17px;font-weight:600;color:var(--white);display:flex;align-items:center;gap:8px}
</style>
</head>
<body>
<div class="flyer">
  <svg class="flyer-art" width="750" height="1060" viewBox="0 0 750 1060">
    <defs>
      <radialGradient id="glow" cx="0.5" cy="0.18" r="0.55">
        <stop offset="0" stop-color="#3a3a3a"/><stop offset="1" stop-color="#000"/>
      </radialGradient>
      <linearGradient id="silver" x1="0" y1="0" x2="1" y2="1">
        <stop offset="0" stop-color="#f2f2f2"/><stop offset=".45" stop-color="#9b9c9e"/><stop offset=".7" stop-color="#e6e6e6"/><stop offset="1" stop-color="#8a8b8d"/>
      </linearGradient>
      <linearGradient id="panelGrad" x1="0" y1="0" x2="0" y2="1">
        <stop offset="0" stop-color="#f0f0f0"/><stop offset="1" stop-color="#d2d3d5"/>
      </linearGradient>
      <linearGradient id="roadPhoto" x1="0" y1="0" x2="0" y2="1">
        <stop offset="0" stop-color="#1b1d26"/><stop offset=".45" stop-color="#232633"/><stop offset=".7" stop-color="#8d7460"/><stop offset="1" stop-color="#c9a489"/>
      </linearGradient>
      <linearGradient id="siteA" x1="0" y1="0" x2="0" y2="1"><stop offset="0" stop-color="#3f78c8"/><stop offset=".55" stop-color="#8a7750"/><stop offset="1" stop-color="#b4562f"/></linearGradient>
      <linearGradient id="siteB" x1="0" y1="0" x2="0" y2="1"><stop offset="0" stop-color="#4a86d0"/><stop offset=".55" stop-color="#c9c6bd"/><stop offset="1" stop-color="#b06a3b"/></linearGradient>
      <linearGradient id="siteC" x1="0" y1="0" x2="0" y2="1"><stop offset="0" stop-color="#8c8a88"/><stop offset=".5" stop-color="#5b4b44"/><stop offset="1" stop-color="#8e4a30"/></linearGradient>
    </defs>
    <rect width="750" height="1060" fill="url(#glow)"/>
    <!-- header rules -->
    <line x1="222" y1="33" x2="527" y2="33" stroke="#bdbdbd" stroke-width="2"/>
    <line x1="225" y1="167" x2="318" y2="167" stroke="#bdbdbd" stroke-width="2"/>
    <line x1="434" y1="167" x2="527" y2="167" stroke="#bdbdbd" stroke-width="2"/>
    <!-- hero photo area -->
    <polygon points="0,206 750,206 750,400 0,505" fill="url(#roadPhoto)" role="img" aria-label="Road train with curtain-side trailer and drop-deck trailers on a red dirt road"/>
    <!-- silver diagonal band -->
    <polygon points="0,505 750,400 750,408 0,547" fill="url(#silver)"/>
    <!-- services panel -->
    <polygon points="403,472 704,417 704,829 403,829" fill="url(#panelGrad)"/>
    <!-- left rules -->
    <!-- photo frames -->
    <g>
      <rect x="37" y="831" width="212" height="123" rx="9" fill="url(#silver)"/>
      <rect x="46" y="839" width="194" height="107" rx="8" fill="url(#siteA)" role="img" aria-label="Loader and water tanker with workers on a red dirt site"/>
      <rect x="263" y="831" width="213" height="123" rx="9" fill="url(#silver)"/>
      <rect x="273" y="839" width="194" height="107" rx="8" fill="url(#siteB)" role="img" aria-label="Side tipper unloading red sand beside a white prime mover"/>
      <rect x="491" y="831" width="213" height="123" rx="9" fill="url(#silver)"/>
      <rect x="501" y="839" width="194" height="107" rx="8" fill="url(#siteC)" role="img" aria-label="Tipper trailer spreading crushed rock on a road build"/>
    </g>
    <!-- phone band -->
    <polygon points="420,1017 436,971 750,971 750,1017" fill="url(#silver)"/>
    <polygon points="420,1017 432,971 440,971 428,1017" fill="#111"/>
    <circle cx="476" cy="994" r="17" fill="#000"/>
    <path d="M469 985c2-2 4-1 5 1l1 3c0 1-1 2-2 3 1 3 3 5 6 6 1-1 2-2 3-2l3 1c2 1 3 3 1 5-3 3-8 2-13-3s-6-10-4-14z" fill="#fff"/>
  </svg>

  <div class="abs brand-name">RUV</div>
  <div class="abs brand-suffix">Pty Ltd</div>

  <div class="abs services-tab">OUR SERVICES</div>
  <ul class="abs services-list">
    <li><svg width="16" height="16" viewBox="0 0 16 16"><circle cx="8" cy="8" r="6.5" fill="none" stroke="#222" stroke-width="1.5"/><path d="M4.5 8l3 3 7-8" fill="none" stroke="#222" stroke-width="2"/></svg>Over size loads/ Hot Shot Loads</li>
    <li><svg width="16" height="16" viewBox="0 0 16 16"><circle cx="8" cy="8" r="6.5" fill="none" stroke="#222" stroke-width="1.5"/><path d="M4.5 8l3 3 7-8" fill="none" stroke="#222" stroke-width="2"/></svg>Heavy Vehicle Recovery Services</li>
    <li><svg width="16" height="16" viewBox="0 0 16 16"><circle cx="8" cy="8" r="6.5" fill="none" stroke="#222" stroke-width="1.5"/><path d="M4.5 8l3 3 7-8" fill="none" stroke="#222" stroke-width="2"/></svg>Potable Water Deliveries</li>
    <li><svg width="16" height="16" viewBox="0 0 16 16"><circle cx="8" cy="8" r="6.5" fill="none" stroke="#222" stroke-width="1.5"/><path d="M4.5 8l3 3 7-8" fill="none" stroke="#222" stroke-width="2"/></svg>Road Building/ Maintenance</li>
    <li><svg width="16" height="16" viewBox="0 0 16 16"><circle cx="8" cy="8" r="6.5" fill="none" stroke="#222" stroke-width="1.5"/><path d="M4.5 8l3 3 7-8" fill="none" stroke="#222" stroke-width="2"/></svg>Earthworks</li>
    <li><svg width="16" height="16" viewBox="0 0 16 16"><circle cx="8" cy="8" r="6.5" fill="none" stroke="#222" stroke-width="1.5"/><path d="M4.5 8l3 3 7-8" fill="none" stroke="#222" stroke-width="2"/></svg>Sand &amp; Metal Supply &amp; Cartage</li>
    <li><svg width="16" height="16" viewBox="0 0 16 16"><circle cx="8" cy="8" r="6.5" fill="none" stroke="#222" stroke-width="1.5"/><path d="M4.5 8l3 3 7-8" fill="none" stroke="#222" stroke-width="2"/></svg>Road Train Tippers</li>
    <li><svg width="16" height="16" viewBox="0 0 16 16"><circle cx="8" cy="8" r="6.5" fill="none" stroke="#222" stroke-width="1.5"/><path d="M4.5 8l3 3 7-8" fill="none" stroke="#222" stroke-width="2"/></svg>Road Train Tankers</li>
    <li><svg width="16" height="16" viewBox="0 0 16 16"><circle cx="8" cy="8" r="6.5" fill="none" stroke="#222" stroke-width="1.5"/><path d="M4.5 8l3 3 7-8" fill="none" stroke="#222" stroke-width="2"/></svg>Road Train Flat Tops</li>
    <li><svg width="16" height="16" viewBox="0 0 16 16"><circle cx="8" cy="8" r="6.5" fill="none" stroke="#222" stroke-width="1.5"/><path d="M4.5 8l3 3 7-8" fill="none" stroke="#222" stroke-width="2"/></svg>Drop Deck Trailers</li>
    <li><svg width="16" height="16" viewBox="0 0 16 16"><circle cx="8" cy="8" r="6.5" fill="none" stroke="#222" stroke-width="1.5"/><path d="M4.5 8l3 3 7-8" fill="none" stroke="#222" stroke-width="2"/></svg>Mine Site accredited<br>equipment &amp; Operators</li>
  </ul>

  <div class="abs capable">WE ARE CAPABLE<br>OF SUPPLYING</div>
  <div class="abs rule" style="left:47px;top:643px;width:250px"></div>
  <div class="abs supply-list">POTABLE WATER,<br>SAND DELIVERIES,<br>OVER SIZE LOADS,<br>EARTHWORKS +MORE</div>
  <div class="abs rule" style="left:47px;top:805px;width:250px"></div>

  <div class="abs note">We offer a large range of services not listed so</div>
  <div class="abs cta">CALL US TODAY FOR A PERSONALISED<br>QUOTE TO SUIT YOUR NEEDS</div>

  <div class="abs phone">043 XXX XXXX</div>
  <div class="abs contact">RUV Pty ltd
    <svg width="13" height="13" viewBox="0 0 13 13"><circle cx="6.5" cy="6.5" r="6.5" fill="#fff"/><rect x="3" y="4.2" width="7" height="4.8" fill="#000"/><path d="M3 4.2l3.5 2.6 3.5-2.6" fill="none" stroke="#fff" stroke-width=".8"/></svg>
    info@ruv.com</div>
</div>
</body>
</html>
```